依頼詳細
「北辰年金事務研究連盟」の概要・活動内容等を紹介するパンフレットの作成です。パンフレットとはいえ、A4裏表の簡易版でOKです(ページ数2ページ)。全体として、固い厳粛なイメージが出ればよいかと思います。記載する文章等は添付ファイルのとおりですので、配置や色、デザイン等の作成をお願いします。アレンジはお任せします。
記載項目
北辰年金事務研究連盟/ごあいさつ/協議会概要/活動内容(原則、添付ファイルの通り)
サイズ
A4
ページ数
両面
希望イメージ
シンプル 複雑
単色 カラフル
暗い 明るい
日常 高級
遊び心 厳粛
未来的 伝統的
女性的 男性的
希望する色
青系、茶系、グレー系、全体のバランスがよければ必ずしも上記に拘らないです。
納品ファイル
• PNG形式 (.png)
補足説明
協議会のWEBサイトは以下です。
http://hokushin-renmei.net/
内容やイメージの参考にしてください。

やや硬いイメージを保ちつつ、シンプルで分かりやすいという点を判断基準として、選択いたしました。ありがとうございます。

この度は、多くのランサーの方からご提案いただき、大変ありがとうございます。改めて感謝申し上げます。
途中、修正依頼させていただいた方におかれましては、実際の選択ポイントからずれた内容で依頼してしまったこともあり、この点、お詫び申し上げます。(私以外の担当の意見も反映したことによるものです。何卒ご容赦ください。)
今後また案件が発生した際には、ご協力いただければ幸いです。
どうぞ宜しくお願いします。

```html
<!DOCTYPE html>
<html lang="ja">
<head>
<meta charset="utf-8">
<title>北辰年金事務研究連盟 ごあいさつ</title>
<link href="https://fonts.googleapis.com/css2?family=Noto+Serif+JP:wght@400;700;900&family=Great+Vibes&display=swap" rel="stylesheet">
<style>
  :root {
    --brown-deep: #4a3426;
    --brown-mid: #6b4e3a;
    --beige: #ece6dc;
    --beige-light: #f6f2ec;
    --ink: #3a2e26;
    --rule: #8a7462;
    --white: #ffffff;
  }
  * { margin: 0; padding: 0; box-sizing: border-box; }
  html, body { width: 845px; height: 1200px; overflow: hidden; background: var(--beige); }
  body { font-family: "Noto Serif JP", serif; color: var(--ink); }
  .page { position: relative; width: 845px; height: 1200px; background: radial-gradient(ellipse at 50% 55%, var(--beige-light), var(--beige) 75%); }
  .masthead {
    position: absolute; left: 0; top: 0; width: 845px; height: 132px;
    background: linear-gradient(180deg, var(--brown-mid), var(--brown-deep));
    color: var(--white);
  }
  .masthead-mark {
    position: absolute; left: 28px; top: 14px; width: 52px; height: 52px;
    border-radius: 50%; background: var(--white); opacity: .9;
  }
  .masthead-name {
    position: absolute; left: 100px; top: 12px;
    font-size: 42px; font-weight: 700; letter-spacing: 2px; line-height: 1.2;
  }
  .masthead-tagline {
    position: absolute; left: 30px; top: 78px;
    font-size: 27px; font-weight: 700; letter-spacing: 1px;
  }
  .heading {
    position: absolute; left: 0; top: 170px; width: 845px; text-align: center;
    font-family: "Great Vibes", cursive; font-size: 64px; color: var(--brown-mid);
  }
  .heading-rule { position: absolute; left: 70px; top: 250px; width: 705px; height: 1px; background: var(--rule); }
  .tree {
    position: absolute; left: 110px; top: 300px; width: 625px; height: 830px;
    background: radial-gradient(ellipse at 50% 40%, rgba(255,255,255,.75), rgba(255,255,255,0) 65%);
  }
  .message {
    position: absolute; left: 145px; top: 430px; width: 560px;
    font-size: 12.5px; line-height: 2; text-align: justify;
  }
  .message p { margin-bottom: 14px; text-indent: 1em; }
  .signature { position: absolute; left: 555px; top: 1040px; font-size: 14px; line-height: 1.9; }
  .signature .title { font-size: 14px; }
  .signature .name { font-size: 18px; letter-spacing: 6px; }
  .signature .name small { font-size: 13px; letter-spacing: 4px; margin-right: 10px; }
  .footer-rule { position: absolute; left: 0; bottom: 0; width: 845px; height: 14px; background: var(--brown-deep); }
</style>
</head>
<body>
<div class="page">
  <header class="masthead">
    <div class="masthead-mark"></div>
    <h1 class="masthead-name">北辰年金事務研究連盟</h1>
    <p class="masthead-tagline">社会調査の専門家「社会保険労務士」による全国組織</p>
  </header>

  <div class="heading">Message</div>
  <div class="heading-rule"></div>

  <div class="tree" role="img" aria-label="淡い白色の大樹のシルエット"></div>

  <section class="message">
    <p>北辰年金事務研究連盟の代表の高槻でございます。</p>
    <p>昨今、年金事務機構による社会保険の加入調査は年々厳しさを増しております。具体的には、法人でありながら社会保険に加入していない、いわゆる「未加入」の事業所や、加入すべき従業員を加入させていない「加入漏れ」といった点に対する指導が強化されています。</p>
    <p>当然ではありますが、今後は、中小規模の企業様においても、社会保険に適正に加入することを前提として、経営を考えていかなければならない時代となりました。</p>
    <p>このような状況を踏まえ、社会保険の調査対応に精通した社会保険労務士がチームを組み、企業様の適正な加入と健全な経営を支援するため、「北辰年金事務研究連盟」を設立させていただいた次第でございます。</p>
    <p>ただ、一方で社会保険の負担が企業様に重くのしかかることも事実です。その中で、「いかにして負担を軽減しながら、適正な形で社会保険に加入することができるか」という観点から、全国の会員が知恵を出し合い、各種サービスをご提案させていただければと考えております。</p>
    <p>当連盟の活動にご期待ください。今後とも宜しくお願い申し上げます。</p>
  </section>

  <div class="signature">
    <div class="title">北辰年金事務研究連盟</div>
    <div class="name"><small>代表</small>高槻 誠一</div>
  </div>

  <div class="footer-rule"></div>
</div>
</body>
</html>
```